Stylish new business card needed!

Hello everyone! I am in need of a new business card design for an alarm company here in Hurricane WV. I have all fonts, color codes and logos provided for you use! We are a young company and like the style of a clean sleek looking business card. Would like it double sided, one side holding the logo and the other with your design!
Target Market(s)
The people that are looking for the newest tech for home automation and security
Industry/Entity Type
Alarm services; Home automation
Contact Information for Business Card
Name of person; position (Sales; Installer); Phone Number (555.419.7362); Employee cell Number; Website (www.GuardedByVelm.example); Employee Email; Double sided
Look and feel
Each slider illustrates characteristics of the customer's brand and the style your logo design should communicate.

```html
<!DOCTYPE html>
<html lang="en">
<head>
<meta charset="utf-8">
<title>Velm Business Card</title>
<link href="https://fonts.googleapis.com/css2?family=Montserrat:wght@400;600;700;800&display=swap" rel="stylesheet">
<style>
  :root {
    --orange: #ff7a3f;
    --white: #ffffff;
    --slate: #8fa3a3;
    --backdrop: #b2b2b2;
  }
  * { margin: 0; padding: 0; box-sizing: border-box; }
  html, body {
    width: 1154px; height: 1200px; overflow: hidden;
    background: var(--backdrop);
    font-family: "Montserrat", sans-serif;
  }
  .card {
    position: absolute;
    left: 207px;
    width: 725px;
    height: 434px;
  }
  .card-front { top: 110px; background: var(--orange); color: var(--white); text-align: center; }
  .card-back { top: 666px; background: var(--white); }

  .front-kicker {
    position: absolute; top: 106px; left: 0; right: 0;
    font-weight: 800; font-size: 37px; letter-spacing: 1px; line-height: 1;
  }
  .front-brand {
    position: absolute; top: 150px; left: 0; right: 0;
    font-weight: 400; font-size: 118px; letter-spacing: 4px; line-height: 1;
  }
  .front-tagline {
    position: absolute; top: 309px; left: 0; right: 0;
    font-weight: 800; font-size: 14px; letter-spacing: 0.6px;
  }

  .back-brand {
    position: absolute; left: 62px; top: 92px;
    font-weight: 400; font-size: 70px; letter-spacing: 3px; line-height: 1;
    color: var(--slate);
  }

  .name-band {
    position: absolute; left: 0; top: 212px;
    width: 341px; height: 77px;
    background: var(--orange); color: var(--white);
    padding: 17px 0 0 59px;
  }
  .person-name { font-weight: 700; font-size: 21px; letter-spacing: 0.8px; line-height: 1.15; }
  .person-role { font-weight: 400; font-size: 15px; line-height: 1.2; }

  .contact-list { position: absolute; left: 378px; top: 201px; list-style: none; }
  .contact-item {
    display: flex; align-items: center; height: 37px;
    font-size: 16px; color: var(--slate); letter-spacing: 0.5px;
  }
  .contact-icon { width: 24px; height: 24px; margin-right: 12px; flex: none; }
</style>
</head>
<body>

<section class="card card-front">
  <p class="front-kicker">GUARDED BY</p>
  <p class="front-brand">VELM</p>
  <p class="front-tagline">AUTOMATION AND SECURITY SERVICES</p>
</section>

<section class="card card-back">
  <p class="back-brand">VELM</p>

  <div class="name-band">
    <p class="person-name">NAME OF PERSON</p>
    <p class="person-role">Installer</p>
  </div>

  <ul class="contact-list">
    <li class="contact-item">
      <svg class="contact-icon" viewBox="0 0 24 24"><path fill="#ff7a3f" d="M6.6 10.8a15 15 0 0 0 6.6 6.6l2.2-2.2c.3-.3.7-.4 1-.2 1.1.4 2.3.6 3.6.6.6 0 1 .4 1 1V20c0 .6-.4 1-1 1A17 17 0 0 1 3 4c0-.6.4-1 1-1h3.5c.6 0 1 .4 1 1 0 1.3.2 2.5.6 3.6.1.3 0 .7-.2 1z"/></svg>
      555 419 7362
    </li>
    <li class="contact-item">
      <svg class="contact-icon" viewBox="0 0 24 24"><rect x="6" y="2" width="12" height="20" rx="2" fill="none" stroke="#ff7a3f" stroke-width="2"/><circle cx="12" cy="18.5" r="1" fill="#ff7a3f"/></svg>
      000 000 0000
    </li>
    <li class="contact-item">
      <svg class="contact-icon" viewBox="0 0 24 24"><g fill="none" stroke="#ff7a3f" stroke-width="2"><circle cx="12" cy="12" r="10"/><ellipse cx="12" cy="12" rx="4.5" ry="10"/><path d="M2 12h20M4 7h16M4 17h16"/></g></svg>
      www.GuardedByVelm.example
    </li>
    <li class="contact-item">
      <svg class="contact-icon" viewBox="0 0 24 24"><rect x="1" y="5" width="22" height="14" fill="#ff7a3f"/><path d="M1 5l11 8 11-8M1 19l8-7M23 19l-8-7" fill="none" stroke="#ffffff" stroke-width="1.5"/></svg>
      info@guardedbyvelm.example
    </li>
  </ul>
</section>

</body>
</html>
```